3 x DIN A4 Flyer, Vorder- und Rückseite
Zielgruppe
Handwerksunternehmen
Aufgabenstellung
Wir benötigen 3 Werbeflyer die in Zeitschriften beigelegt werden. Jeweils DIN A4, Vorderseite beschreibt das Produkt, Rückseite kann zur Bestellung mittels Faxantwort benutzt werden. Profibilder und Text wird vollständig geliefert.

```html
<!DOCTYPE html>
<html lang="de">
<head>
<meta charset="utf-8">
<title>Prospektbox für die Baustelle – Flyer</title>
<link href="https://fonts.googleapis.com/css2?family=Ubuntu:wght@400;500;700&display=swap" rel="stylesheet">
<style>
  :root{
    --blue:#1ea6e0;
    --grey-text:#6d6d6d;
    --grey-dark:#4a4a4a;
    --yellow:#ffe21a;
    --paper:#ffffff;
    --photo-light:#eef3f6;
    --photo-mid:#d5e1e8;
  }
  *{margin:0;padding:0;box-sizing:border-box}
  html,body{width:933px;height:1200px;overflow:hidden;background:var(--paper)}
  body{font-family:"Ubuntu",sans-serif;color:var(--grey-text);position:relative}

  .flyer{position:absolute;inset:0;background:var(--paper)}

  .tab-left{position:absolute;left:40px;top:80px;width:26px;height:54px;background:var(--blue)}
  .band-right{position:absolute;left:505px;top:80px;right:0;height:54px;background:var(--blue)}

  .headline{position:absolute;left:80px;top:72px;width:415px}
  .headline__title{font-size:54px;font-weight:700;color:var(--blue);letter-spacing:-1px;line-height:1;white-space:nowrap}
  .headline__sub{font-size:28px;font-weight:700;color:var(--grey-text);line-height:1.1;margin-top:4px}

  .intro{position:absolute;left:150px;top:258px;width:360px;font-weight:500}
  .intro__lead{font-size:34px;font-weight:700;color:var(--grey-text);line-height:1}
  .intro__lead-text{font-size:20px;line-height:1.1;margin-bottom:22px}
  .intro__highlight{font-size:21px;color:var(--blue);line-height:1.1;margin-bottom:20px}
  .intro__note{font-size:14px;margin-bottom:20px}
  .intro__text{font-size:20px;line-height:1.1;margin-bottom:20px}

  .photo{position:absolute}
  .photo--box{left:520px;top:230px;width:345px;height:430px;
    background:linear-gradient(160deg,var(--photo-light),var(--photo-mid));border-radius:6px}
  .photo--ad{left:75px;top:660px;width:222px;height:235px;
    background:linear-gradient(180deg,var(--photo-light) 0%,var(--photo-mid) 45%,var(--blue) 100%);border-radius:6px}

  .badge{position:absolute;left:525px;top:505px;width:150px;height:150px}

  .benefit{position:absolute;left:355px;width:540px;display:flex;gap:22px;align-items:flex-start}
  .benefit--one{top:730px}
  .benefit--two{top:842px}
  .benefit__icon{width:48px;height:44px;flex:none;margin-top:8px}
  .benefit__text{font-size:20px;font-weight:500;color:var(--grey-dark);line-height:1.25}

  .sender{position:absolute;left:82px;top:1040px;width:300px;font-size:17px;line-height:1.3}
  .sender__name{font-weight:700;color:var(--grey-dark)}
  .sender__address{margin-top:22px;font-size:16px}
  .sender__web{margin-top:20px;font-weight:700;font-size:20px;color:var(--grey-dark)}

  .price-panel{position:absolute;left:396px;top:1005px;right:0;bottom:0;background:var(--blue);
    border-top-left-radius:60px}
  .price{position:absolute;left:447px;top:960px;display:flex;align-items:baseline;gap:10px}
  .price__amount{font-size:84px;font-weight:700;color:var(--yellow);font-style:italic;line-height:1}
  .price__unit{font-size:30px;font-weight:700;color:var(--yellow);font-style:italic}
  .price-panel__terms{position:absolute;left:440px;top:1088px;width:460px;font-size:14px;
    color:var(--grey-dark);line-height:1.35}
</style>
</head>
<body>
<main class="flyer">
  <div class="tab-left"></div>
  <div class="band-right"></div>

  <header class="headline">
    <h1 class="headline__title">PROSPEKTBOX</h1>
    <p class="headline__sub">FÜR DIE BAUSTELLE</p>
  </header>

  <section class="intro">
    <p class="intro__lead">Mit einem Klick</p>
    <p class="intro__lead-text">erwerben Sie zu einem absoluten Sonderpreis</p>
    <p class="intro__highlight">die neue und wetterfeste DIN A4 Hochformat Prospektbox mit Deckel zur Wandmontage</p>
    <p class="intro__note">(Montage-Schrauben sind im Lieferumfang NICHT enthalten)</p>
    <p class="intro__text">oder Pfostenmontage mittels Kunststoffbinder</p>
    <p class="intro__note">(im Lieferumfang enthalten)</p>
    <p class="intro__text">und Hohlkehle an der Rückseite des Displays.</p>
  </section>

  <div class="photo photo--box" role="img" aria-label="Produktfoto: transparente Prospektbox aus Acryl mit aufklappbarem Deckel"></div>

  <svg class="badge" viewBox="0 0 100 100" aria-label="Neu">
    <polygon fill="var(--blue)" points="50,2 58,14 72,8 74,23 89,24 84,38 97,46 86,56 93,70 78,73 77,88 63,84 55,97 45,86 32,94 28,79 13,78 17,64 4,56 15,46 8,32 23,28 25,13 39,17"/>
    <text x="50" y="57" text-anchor="middle" font-family="Ubuntu, sans-serif" font-weight="700" font-size="20" fill="#fff" transform="rotate(-12 50 50)">NEU</text>
  </svg>

  <div class="photo photo--ad" role="img" aria-label="Produktfoto: Prospektbox gefüllt mit blauem Flyer „Ihre Werbung hier“"></div>

  <div class="benefit benefit--one">
    <svg class="benefit__icon" viewBox="0 0 48 44"><path d="M4 24 L16 38 L44 4" fill="none" stroke="var(--blue)" stroke-width="8" stroke-linecap="round" stroke-linejoin="round"/></svg>
    <p class="benefit__text">Die ideale Aussenbox für die Präsentation Ihrer Flyer, Prospekte und Informationen in allen Aussenbereichen.</p>
  </div>
  <div class="benefit benefit--two">
    <svg class="benefit__icon" viewBox="0 0 48 44"><path d="M4 24 L16 38 L44 4" fill="none" stroke="var(--blue)" stroke-width="8" stroke-linecap="round" stroke-linejoin="round"/></svg>
    <p class="benefit__text">Ihre Werbemittel werden durch einen Deckel vor Nässe geschützt. Bohrungen für die Wandmontage vorhanden.</p>
  </div>

  <footer>
    <div class="sender">
      <p class="sender__name">Förderwerk des Leichtbau- und Trockenbauhandwerks mbH</p>
      <p class="sender__address">Lindenhofweg 24<br>90402 Nürnberg</p>
      <p class="sender__web">www.kltr.de</p>
    </div>

    <div class="price-panel"></div>
    <div class="price">
      <span class="price__amount">26,-</span>
      <span class="price__unit">netto</span>
    </div>
    <p class="price-panel__terms">Alle angegebenen Preise verstehen sich in Euro zzgl. der gesetzlichen geltenden Mehrwertsteuer von derzeit 19%. Die Lieferung erfolgt ca.10 Tage nach Bestelleingang. Porto/Verpackung 8,90 Euro</p>
  </footer>
</main>
</body>
</html>
```